Torvane Staffing - Mission Poster Design

We are a staffing and recruiting firm with multiple locations across the US. I am seeking a clean modern design highlighting our Mission Statement: Torvane Staffing...Linking Bright Talent with Bold Employers! This design will be framed and placed at the entrance of all of our offices. My website is www.torvanestaffing.example

Target Market(s)

Will be our company mission with a poster prominently placed in each office.

Industry/Entity Type

Staffing

Requirements
Must have
• Must be professional, clean and eye catching. We want to embrace diversity, so we like a variety of people if people will be a focal part.

```html
<!DOCTYPE html>
<html lang="en">
<head>
<meta charset="UTF-8">
<title>Torvane Staffing – Mission Poster</title>
<link href="https://fonts.googleapis.com/css2?family=Bebas+Neue&family=Montserrat:wght@300;500&family=Roboto:wght@400&display=swap" rel="stylesheet">
<style>
  :root {
    --red: #e3262b;
    --green: #0b7a3e;
    --navy: #27286b;
    --yellow: #f2cc1a;
    --grey: #8a8a8a;
    --paper: #ffffff;
    --illustration-a: #3b4a78;
    --illustration-b: #c9cfdd;
  }
  html, body {
    margin: 0;
    padding: 0;
    overflow: hidden;
  }
  .poster {
    width: 900px;
    height: 1200px;
    background: var(--paper);
    position: relative;
    overflow: hidden;
  }
  .poster > * {
    position: absolute;
    left: 0;
    right: 0;
    margin: 0;
    text-align: center;
  }
  .brand {
    top: 44px;
    height: 70px;
    display: flex;
    align-items: center;
    justify-content: center;
    gap: 12px;
  }
  .brand-dot {
    width: 20px;
    height: 20px;
    border-radius: 50%;
    background: var(--yellow);
  }
  .brand-name {
    font-family: "Montserrat", sans-serif;
    font-weight: 500;
    font-size: 48px;
    color: var(--navy);
    letter-spacing: 1px;
  }
  .headline {
    font-family: "Bebas Neue", sans-serif;
    font-weight: 400;
    line-height: 0.9;
    white-space: nowrap;
  }
  .headline-company {
    top: 162px;
    font-size: 130px;
  }
  .headline-company .red { color: var(--red); }
  .headline-company .green { color: var(--green); }
  .headline-verb {
    top: 289px;
    font-size: 126px;
    color: var(--navy);
  }
  .team-illustration {
    top: 406px;
    left: 171px;
    right: auto;
    width: 558px;
    height: 383px;
    border-radius: 12px;
    background: linear-gradient(180deg, var(--illustration-b) 0%, var(--illustration-a) 55%, var(--illustration-a) 100%);
  }
  .mission-talent {
    top: 815px;
    font-size: 137px;
    color: var(--green);
  }
  .mission-joiner {
    top: 915px;
    font-family: "Montserrat", sans-serif;
    font-weight: 300;
    font-size: 58px;
    line-height: 1;
    color: var(--grey);
    letter-spacing: 3px;
  }
  .mission-employers {
    top: 980px;
    font-size: 96px;
    color: var(--red);
  }
  .web-pill {
    top: 1112px;
    left: 50%;
    right: auto;
    transform: translateX(-50%);
    display: flex;
    align-items: center;
    height: 54px;
    border-radius: 27px;
    background: var(--navy);
    overflow: hidden;
  }
  .web-pill-icon {
    width: 80px;
    height: 54px;
    background: var(--yellow);
    border-radius: 27px 0 0 27px;
    display: flex;
    align-items: center;
    justify-content: center;
  }
  .web-pill-text {
    font-family: "Roboto", sans-serif;
    font-size: 30px;
    color: #ffffff;
    padding: 0 30px 0 22px;
    white-space: nowrap;
  }
</style>
</head>
<body>
  <main class="poster">
    <div class="brand">
      <span class="brand-dot"></span>
      <span class="brand-name">Torvane</span>
    </div>

    <h1 class="headline headline-company"><span class="red">TORVANE</span> <span class="green">STAFFING</span></h1>
    <p class="headline headline-verb">LINKING</p>

    <div class="team-illustration" role="img" aria-label="Illustration of a diverse team of five professionals in navy business suits standing together"></div>

    <p class="headline mission-talent">BRIGHT TALENT</p>
    <p class="mission-joiner">WITH</p>
    <p class="headline mission-employers">BOLD EMPLOYERS!</p>

    <div class="web-pill">
      <span class="web-pill-icon">
        <svg width="34" height="34" viewBox="0 0 34 34" fill="none" stroke="#ffffff" stroke-width="2">
          <circle cx="17" cy="17" r="14"/>
          <ellipse cx="17" cy="17" rx="6" ry="14"/>
          <line x1="3" y1="17" x2="31" y2="17"/>
          <path d="M6 9h22M6 25h22"/>
        </svg>
      </span>
      <span class="web-pill-text">www.torvanestaffing.example</span>
    </div>
  </main>
</body>
</html>
```